Kelbrook Tutoring Flyer Design

I need a flyer for a new company based in Samford Valley called 'Kelbrook Tutoring'. We specialise in Mathematics tutoring for students from grade 5 up to grade twelve. We currently have a logo that has purple as its major colour. The final design should convey professionalism, compassion and that education is about maximising peoples possibilities,
Updates

Just thought I would let you know that my slogan is "Maximise your possibilities" and my phone number is 0438260917

Thanks.

My current logo doesn't seem to want to upload

Target Market(s)

The two targets are parents of students in grades 5-12 and students in grades 5-12

Industry/Entity Type

Education

Logo Text

Kelbrook Tutoring

Logo styles of interest
Pictorial/Combination Logo
Abstract Logo
Lettermark Logo
Requirements
Must have
• My slogan is "Maximise your possibilities"
my phone number is 0438260917

```html
<!DOCTYPE html>
<html lang="en">
<head>
<meta charset="utf-8">
<title>Kelbrook Tutoring Flyer Design</title>
<link rel="stylesheet" href="https://fonts.googleapis.com/css2?family=Cinzel:wght@400;600&family=Italianno&family=Source+Sans+3:wght@400;600;700&display=swap">
<style>
  :root {
    --purple: #9b92c4;
    --purple-text: #6a5fa3;
    --plum-dark: #4e1d45;
    --plum-mid: #7e3f6f;
    --orange: #f8a94a;
    --grey-band: #b5b5b7;
    --grey-ring: #d9d9db;
    --grey-panel: #dfe0e3;
    --ink: #1d1d1f;
    --black: #050505;
    --white: #ffffff;
    --footer-mute: #d6d6d6;
  }
  html, body {
    margin: 0;
    padding: 0;
    width: 933px;
    height: 1200px;
    overflow: hidden;
    background: var(--white);
  }
  .flyer {
    position: relative;
    width: 933px;
    height: 1200px;
    overflow: hidden;
    background: var(--grey-panel);
  }
  .flyer-art {
    position: absolute;
    inset: 0;
  }
  .brand-name {
    position: absolute;
    left: 568px;
    top: 108px;
    margin: 0;
    font-family: "Italianno", cursive;
    font-weight: 400;
    font-size: 62px;
    line-height: 1;
    color: var(--ink);
  }
  .slogan {
    position: absolute;
    left: 68px;
    top: 558px;
    width: 340px;
    margin: 0;
    text-align: center;
    font-family: "Cinzel", serif;
    font-weight: 400;
    font-size: 36px;
    line-height: 44px;
    letter-spacing: 1px;
    text-transform: uppercase;
    color: var(--white);
    text-shadow: 0 1px 3px rgba(0,0,0,0.35);
  }
  .speciality {
    position: absolute;
    left: 436px;
    top: 718px;
    width: 420px;
    text-align: center;
    font-family: "Cinzel", serif;
    color: var(--white);
  }
  .speciality-lead {
    margin: 0;
    font-size: 32px;
    line-height: 40px;
    font-weight: 400;
  }
  .speciality-subject {
    margin: 34px 0 0;
    font-size: 42px;
    line-height: 46px;
    font-weight: 600;
  }
  .speciality-grades {
    margin: 40px 0 0;
    font-size: 32px;
    line-height: 37px;
    font-weight: 400;
  }
  .mission {
    position: absolute;
    left: 70px;
    top: 802px;
    width: 330px;
    font-family: "Source Sans 3", sans-serif;
    color: var(--ink);
  }
  .mission-heading {
    margin: 0 0 32px;
    font-size: 23px;
    line-height: 27px;
    font-weight: 700;
    color: var(--purple-text);
  }
  .mission-list {
    list-style: none;
    margin: 0;
    padding: 0;
    font-size: 23px;
    line-height: 26px;
  }
  .mission-list li {
    position: relative;
    padding-left: 18px;
    margin-bottom: 11px;
  }
  .mission-list li::before {
    content: "";
    position: absolute;
    left: 0;
    top: 10px;
    width: 8px;
    height: 8px;
    border-radius: 50%;
    background: var(--orange);
  }
  .mission-list strong {
    font-weight: 700;
  }
  .contact-bar {
    position: absolute;
    left: 0;
    top: 1068px;
    width: 933px;
    height: 132px;
    background: var(--black);
  }
  .contact-name {
    position: absolute;
    left: 75px;
    top: 38px;
    margin: 0;
    font-family: "Cinzel", serif;
    font-size: 30px;
    letter-spacing: 1px;
    color: var(--white);
  }
  .contact-details {
    position: absolute;
    right: 68px;
    top: 36px;
    text-align: right;
    font-family: "Source Sans 3", sans-serif;
  }
  .contact-phone {
    display: block;
    font-size: 32px;
    line-height: 36px;
    color: var(--orange);
  }
  .contact-email {
    display: block;
    font-size: 20px;
    line-height: 26px;
    color: var(--footer-mute);
  }
</style>
</head>
<body>
<main class="flyer">
  <svg class="flyer-art" width="933" height="1200" viewBox="0 0 933 1200">
    <defs>
      <linearGradient id="photoTones" x1="0" y1="0" x2="1" y2="0.3">
        <stop offset="0" stop-color="#b79a92"/>
        <stop offset="0.35" stop-color="#8c6a5a"/>
        <stop offset="0.6" stop-color="#c9a487"/>
        <stop offset="1" stop-color="#e7dccf"/>
      </linearGradient>
      <radialGradient id="plumTones" cx="0.45" cy="0.35" r="0.7">
        <stop offset="0" stop-color="#7e3f6f"/>
        <stop offset="1" stop-color="#4e1d45"/>
      </radialGradient>
      <clipPath id="plumClip">
        <rect x="0" y="195" width="933" height="550"/>
      </clipPath>
    </defs>

    <rect x="0" y="0" width="933" height="195" fill="var(--white)"/>
    <rect x="0" y="0" width="933" height="21" fill="var(--grey-band)"/>

    <path role="img" aria-label="Photo: smiling student leaning over open maths workbooks with a pen"
          d="M0 195 H790 Q890 200 933 275 V620 Q850 640 800 720 H0 Z"
          fill="url(#photoTones)"/>

    <g clip-path="url(#plumClip)">
      <circle cx="250" cy="715" r="310" fill="url(#plumTones)" opacity="0.93"/>
    </g>

    <rect x="-10" y="742" width="412" height="20" rx="10" fill="var(--orange)"/>

    <circle cx="-10" cy="1075" r="85" fill="var(--grey-band)"/>

    <g class="brand-mark" role="img" aria-label="Kelbrook Tutoring brand mark">
      <circle cx="145" cy="133" r="100" fill="var(--grey-ring)"/>
      <circle cx="145" cy="133" r="90" fill="var(--purple)"/>
    </g>

    <circle cx="646" cy="868" r="218" fill="#eeeeef"/>
    <circle cx="646" cy="868" r="208" fill="var(--orange)"/>
    <line x1="462" y1="778" x2="830" y2="778" stroke="var(--white)" stroke-width="2"/>
    <line x1="462" y1="908" x2="830" y2="908" stroke="var(--white)" stroke-width="2"/>
  </svg>

  <h1 class="brand-name">Kelbrook Tutoring</h1>

  <p class="slogan">Maximise your<br>possibilities.</p>

  <section class="speciality">
    <p class="speciality-lead">Specialising in</p>
    <p class="speciality-subject">MATHEMATICS<br>TUTORING</p>
    <p class="speciality-grades">FROM GRADE 5<br>TO GRADE 12</p>
  </section>

  <section class="mission">
    <h2 class="mission-heading">Our mission is to enhance<br>students’ confidence by:</h2>
    <ul class="mission-list">
      <li><strong>valuing</strong> the individual</li>
      <li><strong>increasing</strong> each student’s competence</li>
      <li><strong>having fun</strong> while doing it.</li>
    </ul>
  </section>

  <footer class="contact-bar">
    <p class="contact-name">CALL DANIEL MARSH</p>
    <div class="contact-details">
      <span class="contact-phone">0438 260 917</span>
      <span class="contact-email">kelbrooktutoring@mailpost.com</span>
    </div>
  </footer>
</main>
</body>
</html>
```